Event Poster - Tarona Mist Fest 2018 (Need ASAP)

Create a poster for an upcoming vape event, located in Waikato, Hamilton, New Zealand.

Mist Fest is an event where lots of shops come to a location, and the public are welcomed and they all vape, buy vape products, socialize, drink beer and have fun.

VISIT THE EVENT WEBSITE FOR INFO - www.taronamistfest.co.nz

We have created a website at, as you can see the logo and design is a bit boring and plain, so we dont really want it to look anything like that, The logo that is created to suit the poster will be able to be

Need a poster done up so we can send it around, post it up on boards, share on social media etc

I have attached previous events from nearby towns, for reference, but I want something much better.

Target Market(s)

25-45 Male / Female

Requirements
Must have
• - Tarona Mist Fest 2018
• - Saturday, 2nd June 2018
• - 12-10pm
• - R18 Event (important for public to know)
• - Vendors, Prizes, Comps, E Juice Awards, Entertainment, Giveaways & More
• - The Corner Alehouse (52 Mulgrave Rd, Kerepuni, Hamilton)
• - mention something along lines "Come To Tarona's First Mist Fest"
• - "Get Your Tickets from www.taronamistfest.co.nz TODAY"
• - I want people to know they can buy it from a store as well "The Cloud Barn"
Nice to have
• Our City colors are Red,Yellow,Black which is symbolic for "Waikato" so it would be nice to have those integrated in there. Alot of the other Mist Fest events have dark, bogan, amateur look done to them, so I want ours to be just a much better version.
• To Clarify, Hamilton is a city inside the Waikato
• I might want to put sponsors on there as well, possibly 10-20, but maybe only a few if space is a problem

```html
<!DOCTYPE html>
<html lang="en">
<head>
<meta charset="utf-8">
<title>Tarona Mist Fest 2018 – Event Poster</title>
<link rel="stylesheet" href="https://fonts.googleapis.com/css2?family=Anton&family=Audiowide&family=Oswald:wght@600;700&family=Roboto+Condensed:wght@400;700&display=swap">
<style>
  :root {
    --backdrop: #a9a9a9;
    --ink: #050505;
    --white: #ffffff;
    --red: #dc1a1a;
    --bright-red: #ff1a1a;
    --yellow: #ffcc00;
    --tan: #c9a86a;
    --line: #e6e6e6;
  }
  * { box-sizing: border-box; margin: 0; padding: 0; }
  html, body { width: 1200px; height: 1200px; overflow: hidden; }
  body { background: var(--backdrop); position: relative; font-family: "Roboto Condensed", sans-serif; }

  .poster {
    position: absolute; left: 172px; top: 0; width: 856px; height: 1200px;
    background:
      radial-gradient(ellipse at 15% 20%, rgba(90,90,90,.35), transparent 45%),
      radial-gradient(ellipse at 85% 90%, rgba(90,90,90,.3), transparent 40%),
      var(--ink);
    overflow: hidden;
  }
  .poster > * { position: absolute; }

  .title-place { left: 76px; top: 46px; font-family: "Audiowide", sans-serif; font-size: 60px; color: var(--yellow); letter-spacing: 2px; line-height: 1; }
  .title-year { left: 74px; top: 128px; font-family: "Anton", sans-serif; font-size: 190px; color: var(--white); line-height: 1; letter-spacing: 2px; }
  .title-event { left: 523px; top: 46px; font-family: "Anton", sans-serif; font-size: 128px; color: var(--red); line-height: 1; }
  .title-event span { display: block; }
  .title-event span + span { margin-top: 6px; }

  .time-frame { left: 122px; top: 356px; width: 611px; height: 151px; border: 2px solid var(--line); }
  .time-badge { left: 274px; top: 340px; width: 308px; height: 78px; background: var(--yellow); color: var(--ink); font-family: "Oswald", sans-serif; font-weight: 700; font-size: 60px; line-height: 78px; text-align: center; }
  .event-date { left: 122px; top: 440px; width: 611px; text-align: center; color: var(--white); font-size: 48px; line-height: 1.1; }

  .smoke { top: 520px; height: 110px; width: 190px; }
  .smoke-left { left: 0; background: radial-gradient(ellipse at 70% 50%, rgba(200,120,40,.55), rgba(60,80,180,.3) 45%, transparent 70%); }
  .smoke-right { right: 0; background: radial-gradient(ellipse at 30% 50%, rgba(200,120,40,.55), rgba(60,80,180,.3) 45%, transparent 70%); }

  .age-notice { left: 0; width: 856px; top: 540px; text-align: center; font-family: "Oswald", sans-serif; font-weight: 700; font-size: 108px; line-height: 1; color: var(--yellow); transform: scaleY(1.05); }

  .features { left: 0; width: 856px; top: 668px; text-align: center; color: var(--white); font-size: 35px; line-height: 44px; }
  .features .dot { color: var(--red); font-size: 24px; vertical-align: middle; margin: 0 8px; }

  .venue { left: 122px; top: 780px; width: 611px; height: 54px; border: 2px solid var(--line); color: var(--yellow); font-size: 21px; line-height: 50px; padding-left: 62px; white-space: nowrap; overflow: hidden; letter-spacing: -0.2px; }
  .venue-pin { left: 108px; top: 778px; width: 58px; height: 58px; }

  .invite { left: 0; width: 856px; top: 862px; text-align: center; font-family: "Oswald", sans-serif; font-weight: 700; font-size: 42px; color: var(--white); line-height: 1.2; }
  .invite em { font-style: normal; color: var(--bright-red); }

  .brand-mark { left: 47px; top: 960px; width: 240px; display: flex; align-items: center; gap: 14px; }
  .brand-mark .block { width: 70px; height: 190px; background: var(--yellow); flex: none; }
  .brand-mark .name { font-family: "Roboto Condensed", sans-serif; font-weight: 700; font-size: 40px; line-height: 1.05; color: var(--white); }

  .tickets-lead { left: 434px; top: 966px; color: var(--white); font-size: 23px; }
  .tickets-url { left: 434px; top: 994px; color: var(--yellow); font-size: 23px; font-weight: 700; white-space: nowrap; }
  .tickets-url em { font-style: normal; color: var(--bright-red); font-weight: 400; }
  .ticket-art { left: 434px; top: 1035px; width: 210px; height: 89px; background: linear-gradient(135deg, #d8bd85, var(--tan)); }
  .ticket-link { left: 640px; top: 1012px; }
  .store-note { left: 432px; top: 1135px; color: var(--white); font-size: 16px; white-space: nowrap; }
  .store-note em { font-style: normal; color: var(--bright-red); font-weight: 700; }
</style>
</head>
<body>
  <main class="poster">
    <div class="title-place">TARONA</div>
    <div class="title-year">2018</div>
    <div class="title-event"><span>MIST</span><span>FEST</span></div>

    <div class="time-frame"></div>
    <div class="time-badge">12-10pm</div>
    <div class="event-date">Saturday, 2nd June 2018</div>

    <div class="smoke smoke-left" role="img" aria-label="Coloured smoke wisp"></div>
    <div class="smoke smoke-right" role="img" aria-label="Coloured smoke wisp"></div>
    <div class="age-notice">R18 EVENT</div>

    <div class="features">
      <p>Vendor<span class="dot">•</span>Prize<span class="dot">•</span>Comp<span class="dot">•</span>E Juice Awards</p>
      <p>Entertainment<span class="dot">•</span>Giveaways &amp; More</p>
    </div>

    <div class="venue">The Corner Alehouse (52 Mulgrave Rd, Kerepuni, Hamilton)</div>
    <svg class="venue-pin" viewBox="0 0 58 58" aria-hidden="true">
      <circle cx="29" cy="29" r="28" fill="#fff"/>
      <path d="M29 14c-6 0-10 4.5-10 10 0 7 10 18 10 18s10-11 10-18c0-5.5-4-10-10-10z" fill="#e11"/>
      <circle cx="29" cy="24" r="4" fill="#fff"/>
    </svg>

    <div class="invite">Come To Tarona's <em>First Mist Fest</em></div>

    <div class="brand-mark">
      <div class="block"></div>
      <div class="name">Tarona<br>Mist<br>Fest<br>2018</div>
    </div>

    <div class="tickets-lead">Get Your Tickets from</div>
    <div class="tickets-url">www.taronamistfest.co.nz <em>TODAY</em></div>
    <svg class="ticket-link" width="180" height="72" viewBox="0 0 180 72" aria-hidden="true">
      <polyline points="150,2 177,2 177,67 2,67" fill="none" stroke="#e6e6e6" stroke-width="1.5"/>
    </svg>
    <div class="ticket-art" role="img" aria-label="Admission ticket reading Get Your Tickets Now"></div>
    <div class="store-note">People can buy it from a store as well "<em>The Cloud Barn</em>"</div>
  </main>
</body>
</html>
```